Redesign of a Brochure based on an exsiting example for Web download and email marketing

Can you create a professional brochure based on the attached PDF. We need to keep the name, the logo and the content but everything else can be changed . The PDF will primarily be will be used for web download and email marking but it aslo be printed out for a poster design will be appropriate

Target Market(s)

Business to Business

Industry/Entity Type

Marketing

Font styles to use
Serif

Requirements
Must have
• Must have the existing logo ( in the attached document) and contain the same content

```html
<!DOCTYPE html>
<html lang="en">
<head>
<meta charset="utf-8">
<title>IT RUN Model 1 – Veralyn</title>
<link rel="stylesheet" href="https://fonts.googleapis.com/css2?family=Raleway:wght@400;500;600;700&family=Roboto:wght@300;400&display=swap">
<style>
  :root {
    --navy: #1c3461;
    --panel-blue: #4b7fc0;
    --panel-blue-light: #6592ca;
    --accent-blue: #3a73c2;
    --title-navy: #14294f;
    --body-text: #2e2e2e;
    --muted: #6b6b6b;
    --ring: #7a7a7a;
    --white: #ffffff;
    --slice-apps: #fcc862;
    --slice-help: #ad86c0;
    --slice-unalloc: #b6d96a;
    --slice-network: #87cdf0;
    --slice-euc: #ef7274;
    --slice-dc: #f6f18c;
  }
  * { margin: 0; padding: 0; box-sizing: border-box; }
  html, body { width: 1200px; height: 900px; overflow: hidden; background: var(--white); }
  body { font-family: "Raleway", sans-serif; font-variant-numeric: lining-nums; color: var(--body-text); position: relative; }

  .page { position: relative; width: 1200px; height: 900px; }

  .model-heading { position: absolute; left: 57px; top: 72px; width: 763px; }
  .model-label { font-size: 25px; font-weight: 400; color: var(--accent-blue); line-height: 30px; }
  .model-name { font-size: 26px; font-weight: 700; color: var(--title-navy); line-height: 32px; }
  .heading-rule { position: absolute; left: 57px; top: 139px; width: 763px; height: 2px; background: var(--accent-blue); }

  .intro { position: absolute; left: 57px; top: 163px; width: 763px; font-family: "Roboto", sans-serif; font-weight: 300; font-size: 15.6px; line-height: 20px; text-align: justify; color: #222; }
  .intro p { margin-bottom: 20px; }
  .intro ul { list-style: none; margin: 2px 0 17px; }
  .intro li { padding-left: 19px; position: relative; line-height: 25px; }
  .intro li::before { content: "•"; position: absolute; left: 3px; font-size: 17px; }
  .intro p.tight { margin-bottom: 0; }

  .towers-title { position: absolute; left: 57px; top: 594px; font-size: 19px; line-height: 23px; color: var(--title-navy); font-weight: 500; }
  .towers-rule { position: absolute; left: 57px; top: 657px; width: 178px; height: 2px; background: var(--accent-blue); }

  .tower-chart { position: absolute; left: 0; top: 0; }
  .chart-label { font-family: "Raleway", sans-serif; font-size: 13px; fill: var(--muted); }

  .page-number { position: absolute; left: 57px; top: 843px; width: 40px; height: 57px; background: var(--panel-blue); color: var(--white); font-size: 17px; display: flex; align-items: center; justify-content: center; }
  .footnote { position: absolute; right: 380px; top: 864px; font-size: 10px; color: var(--muted); }
  .footnote strong { color: var(--title-navy); font-weight: 600; }

  .brand-block { position: absolute; left: 877px; top: 0; width: 276px; height: 142px; background: var(--navy); color: var(--white); }
  .brand-mark { position: absolute; left: 26px; top: 59px; width: 20px; height: 30px; border: 2px solid var(--white); }
  .brand-name { position: absolute; left: 76px; top: 60px; font-size: 24px; letter-spacing: 5px; font-weight: 500; }
  .brand-tagline { position: absolute; left: 86px; top: 97px; font-size: 15.5px; font-weight: 400; }

  .info-panel { position: absolute; left: 877px; top: 167px; width: 276px; height: 733px; background: var(--panel-blue); color: var(--white); }
  .panel-wash { position: absolute; inset: 0; background: linear-gradient(160deg, var(--panel-blue-light) 0%, var(--panel-blue) 65%); }
  .meta { position: absolute; left: 14px; top: 394px; }
  .meta dt { font-size: 16px; font-weight: 600; line-height: 20px; }
  .meta dd { font-size: 16px; font-weight: 400; line-height: 20px; margin-bottom: 20px; }
</style>
</head>
<body>
<div class="page">

  <header class="model-heading">
    <div class="model-label">Model Name:</div>
    <h1 class="model-name">IT RUN Model 1</h1>
  </header>
  <div class="heading-rule"></div>

  <section class="intro">
    <p>IT Run Model 1 is a simple IT costing model suitable for any industry. It is designed to support a sophisticated level of cost transparency across common IT technologies, towers and services with a minimum of effort. As a starting point this model is mainly focused on the IT costs that “run” the business. However, it can be extended to cover a detailed view of IT investments that “change” the business as well. In addition, it can be used as a starting point to manage demand by extending support for specific business processes.</p>
    <p>This model is a concrete implementation of the Technology Business Management (TBM) standard framework.*</p>
    <p class="tight">TBM has three main views:</p>
    <ul>
      <li>Finance View,</li>
      <li>IT View,</li>
      <li>Business view.</li>
    </ul>
    <p class="tight">This model implements these views through three simple layers; IT Cost centres, IT Technology Towers and Products &amp; Services.</p>
    <p>You can start by implementing just the IT Cost Centres to get some valuable insights before moving on to the IT Towers and Product/Services layers.</p>
  </section>

  <h2 class="towers-title">Tech Towers<br>(Run Build Manage)</h2>
  <div class="towers-rule"></div>

  <svg class="tower-chart" width="877" height="840" viewBox="0 0 877 840" role="img" aria-label="Pie chart of tech tower cost split">
    <g stroke="#ffffff" stroke-width="2" stroke-linejoin="round">
      <path d="M520 678 L487 596.4 A88 88 0 0 1 607.7 670.3 Z" fill="var(--slice-apps)"/>
      <path d="M520 678 L607.7 670.3 A88 88 0 0 1 599.8 715.2 Z" fill="var(--slice-help)"/>
      <path d="M520 678 L599.8 715.2 A88 88 0 0 1 594.6 724.6 Z" fill="var(--slice-unalloc)"/>
      <path d="M520 678 L594.6 724.6 A88 88 0 0 1 447.9 728.5 Z" fill="var(--slice-network)"/>
      <path d="M520 678 L447.9 728.5 A88 88 0 0 1 435 655.2 Z" fill="var(--slice-euc)"/>
      <path d="M520 678 L435 655.2 A88 88 0 0 1 487 596.4 Z" fill="var(--slice-dc)"/>
    </g>
    <circle cx="520" cy="678" r="96" fill="none" stroke="var(--ring)" stroke-width="4" stroke-dasharray="95 6"/>
    <g stroke="var(--ring)" stroke-width="2">
      <line x1="580" y1="604" x2="594" y2="592"/>
      <line x1="616" y1="672" x2="628" y2="671"/>
      <line x1="604" y1="722" x2="617" y2="729"/>
      <line x1="478" y1="764" x2="473" y2="773"/>
      <line x1="426" y1="696" x2="414" y2="698"/>
      <line x1="442" y1="624" x2="431" y2="615"/>
    </g>
    <g stroke="var(--ring)" stroke-width="2">
      <circle cx="597" cy="590" r="5" fill="var(--slice-apps)"/>
      <circle cx="633" cy="671" r="5" fill="var(--slice-help)"/>
      <circle cx="621" cy="731" r="5" fill="var(--slice-unalloc)"/>
      <circle cx="472" cy="776" r="5" fill="var(--slice-network)"/>
      <circle cx="410" cy="698" r="5" fill="var(--slice-euc)"/>
      <circle cx="427" cy="613" r="5" fill="var(--slice-dc)"/>
    </g>
    <text class="chart-label" x="613" y="594">Apps Maintenance</text>
    <text class="chart-label" x="647" y="675">Helpdesk &amp; Ops Bridge</text>
    <text class="chart-label" x="636" y="737">Not Allocated</text>
    <text class="chart-label" x="415" y="800">Networks &amp; Telecoms</text>
    <text class="chart-label" x="269" y="705">End User Computing</text>
    <text class="chart-label" x="285" y="614">Datacentre &amp; Serves</text>
  </svg>

  <div class="page-number">1</div>
  <p class="footnote">* For Technology Business Management (TBM) see <strong>itvalueforum.org</strong></p>

  <aside class="brand-block">
    <div class="brand-mark"></div>
    <div class="brand-name">VERALYN</div>
    <div class="brand-tagline">IT Cost Transparency</div>
  </aside>

  <aside class="info-panel">
    <div class="panel-wash" role="img" aria-label="Soft blue decorative background"></div>
    <dl class="meta">
      <dt>Date Published:</dt><dd>05 June 2015</dd>
      <dt>Published Model Number:</dt><dd>100001</dd>
      <dt>Author:</dt><dd>Veralyn</dd>
      <dt>Contact:</dt><dd>rnorwood@ashbyfield.co.uk</dd>
      <dt>Related models:</dt><dd>IT Build Model 1 - 100002</dd>
    </dl>
  </aside>

</div>
</body>
</html>
```